Brightwell Giving Inc

We need a full re-design of our non-profit organization website (www.brightwellgiving.org). Ideally, we are looking to make it more attractive, user-friendly, and interactive with our business model.

Please make sure to user colors that ago with our logo.

We need a homepage done and we also need a content page done where we will use for the other pages to fill with content.

Target Market(s)

Clothes/textiles donations.

Industry/Entity Type

Charity

Number of Pages Required

2 page

Colors

Designer to choose colors to be used in the design.

Requirements
Must have
• It must match the styling of our logo and same colors as current website. (www.brightwellgiving.org)
Nice to have
• Sleek homepage that is easy to understand and get our main points across.

```html
<!DOCTYPE html>
<html lang="en">
<head>
<meta charset="utf-8">
<title>Brightwell Giving – Home</title>
<link href="https://fonts.googleapis.com/css2?family=Roboto:wght@400;500;700&family=Roboto+Condensed:wght@400;700&display=swap" rel="stylesheet">
<style>
:root{
  --green-dark:#2f5d14;
  --green:#3f7a1c;
  --green-mid:#5a9a2a;
  --green-light:#d7edc2;
  --green-pale:#e6f4d8;
  --yellow:#f6c800;
  --yellow-deep:#f2b600;
  --red:#d7141c;
  --grey-bg:#efefef;
  --ink:#222;
  --muted:#555;
  --footer:#222222;
  --white:#fff;
}
*{box-sizing:border-box;margin:0;padding:0}
html,body{width:1200px;height:3766px;overflow:hidden}
body{font-family:"Roboto",Arial,sans-serif;color:var(--ink);position:relative;background:var(--white)}
.abs{position:absolute}
.cond{font-family:"Roboto Condensed","Arial Narrow",sans-serif}
.btn-more{display:inline-block;background:var(--green-dark);color:#fff;font:700 13px "Roboto Condensed",sans-serif;padding:8px 16px;border-radius:3px;letter-spacing:.3px}

/* header */
.site-header{position:absolute;left:0;top:0;width:1200px;height:85px;background:var(--yellow)}
.brand{position:absolute;left:188px;top:22px;display:flex;align-items:center;gap:10px}
.brand-mark{width:40px;height:40px;background:var(--green-dark);border-radius:4px}
.brand-name{font:700 24px "Roboto Condensed",sans-serif;color:var(--green-dark);line-height:1}
.brand-tag{font-size:12px;color:var(--green-dark);margin-top:4px}
.phone-icon{position:absolute;left:545px;top:25px}
.phone{position:absolute;top:20px;font:500 15px "Roboto",sans-serif;color:var(--green-dark);line-height:1.3}
.phone b{font-size:18px;display:block}
.donate-now{position:absolute;left:886px;top:24px;width:146px;height:38px;background:var(--red);color:#fff;border-radius:20px;font:700 16px "Roboto Condensed",sans-serif;text-align:center;line-height:38px}

.main-nav{position:absolute;left:0;top:85px;width:1200px;height:45px;background:var(--green-light);display:flex;align-items:center;padding-left:175px;gap:0}
.main-nav a{font:500 13px "Roboto",sans-serif;color:var(--green-dark);padding:0 18px;height:33px;line-height:33px;text-decoration:none}
.main-nav a.active{background:var(--green);color:#fff;border-radius:2px}

/* hero */
.hero{position:absolute;left:0;top:130px;width:1200px;height:568px;background:linear-gradient(160deg,#5d7a4a 0%,#8a9a7a 35%,#b7a89a 60%,#5c6b55 100%)}
.hero-title{position:absolute;left:0;top:195px;width:1200px;text-align:center;color:#fff;text-shadow:0 2px 6px rgba(0,0,0,.5)}
.hero-title .line1{font:400 40px "Roboto Condensed",sans-serif}
.hero-title .line2{font:700 40px "Roboto Condensed",sans-serif;margin-top:8px}
.bin-visual{position:absolute;left:188px;top:440px;width:130px;height:120px;background:linear-gradient(#3fae3c,#237a22);border-radius:4px}
.finder{position:absolute;left:0;top:503px;width:1200px;height:65px;background:var(--green);display:flex;align-items:center}
.finder-label{position:absolute;left:340px;top:20px;color:#fff;font:500 19px "Roboto",sans-serif;display:flex;gap:12px;align-items:center}
.finder-input{position:absolute;left:658px;top:16px;width:190px;height:34px;background:var(--green-mid);color:#cfe6b8;font-size:14px;padding:8px 10px}
.finder-btn{position:absolute;left:853px;top:16px;width:100px;height:34px;background:var(--yellow);color:var(--green-dark);font:700 14px "Roboto Condensed",sans-serif;text-align:center;line-height:34px}

/* welcome */
.welcome{position:absolute;left:0;top:698px;width:1200px;height:377px;background:#fff}
.welcome h2{position:absolute;left:0;top:60px;width:1200px;text-align:center;font:400 32px "Roboto Condensed",sans-serif;display:flex;justify-content:center;align-items:center;gap:10px}
.welcome h2 b{color:var(--green-dark);font-weight:700}
.welcome h2 i{width:36px;height:36px;background:var(--green-dark);display:inline-block;border-radius:4px}
.welcome p{position:absolute;left:188px;top:140px;width:824px;text-align:center;font-size:13px;line-height:2;color:var(--muted)}
.welcome .btn-more{position:absolute;left:557px;top:292px}

/* features */
.values{position:absolute;left:0;top:1075px;width:1200px;height:446px;background:linear-gradient(120deg,#4a4e4c 0%,#6b6d5f 40%,#3d4a3a 70%,#2b2f2c 100%)}
.value-card{position:absolute;width:208px;height:98px;background:rgba(214,238,194,.88);border-radius:3px;padding:20px 14px 0 54px;font:500 15px "Roboto",sans-serif;color:var(--green-dark);line-height:1.35}
.value-card::before{content:"\201C";position:absolute;left:12px;top:22px;width:30px;height:30px;border-radius:50%;background:var(--yellow);color:var(--green-dark);font:700 26px Georgia,serif;text-align:center;line-height:36px}

/* recipients */
.recipients{position:absolute;left:0;top:1521px;width:1200px;height:506px;background:var(--grey-bg)}
.rec-mark{position:absolute;left:338px;top:62px;width:74px;height:74px;background:var(--green-dark);border-radius:6px}
.recipients h2{position:absolute;left:200px;top:145px;width:350px;text-align:center;font:700 32px "Roboto Condensed",sans-serif;color:var(--green-dark)}
.recipients .sub{position:absolute;left:200px;top:190px;width:350px;text-align:center;font-size:15px;color:var(--muted)}
.recipients .btn-more{position:absolute;left:326px;top:236px}
.bar{position:absolute;background:var(--yellow);bottom:72px}
.bar::after{content:"";position:absolute;left:50%;bottom:12px;width:26px;height:22px;margin-left:-13px;background:var(--green-dark);border-radius:3px}
.level{position:absolute;width:146px;height:52px;background:var(--green-mid);border-radius:3px;color:#fff;text-align:center;font-family:"Roboto Condensed",sans-serif;padding-top:6px}
.level small{display:block;font-size:13px}
.level b{display:block;font-size:18px}
.baseline{position:absolute;left:427px;top:1955px;width:678px;height:4px;background:var(--yellow)}

/* how it works */
.how{position:absolute;left:0;top:2027px;width:1200px;height:463px;background:var(--green)}
.how-top{position:absolute;left:0;top:-5px;width:1200px;height:8px;background:var(--green-dark)}
.how .ghost{position:absolute;left:0;top:20px;width:1200px;text-align:center;font:700 34px "Roboto Condensed",sans-serif;color:rgba(0,0,0,.13);letter-spacing:1px}
.how-ribbon{position:absolute;left:440px;top:46px;width:320px;height:40px;background:#fff;color:var(--green-dark);text-align:center;font:700 26px "Roboto Condensed",sans-serif;line-height:40px}
.how-rule{position:absolute;top:66px;height:2px;width:70px;background:#fff}
.step{position:absolute;top:137px;width:260px;text-align:center;color:#fff}
.step-circle{width:140px;height:140px;margin:0 auto;border-radius:50%;background:var(--yellow);position:relative;display:flex;align-items:center;justify-content:center}
.step-circle .inner{width:112px;height:112px;border-radius:50%;background:#fff;display:flex;align-items:center;justify-content:center}
.step-num{position:absolute;left:-10px;top:4px;width:46px;height:46px;border-radius:50%;background:var(--red);color:#fff;font:700 18px "Roboto Condensed",sans-serif;line-height:46px;border:3px solid #fff}
.step p{margin-top:22px;font-size:15px;line-height:1.45}
.how .btn-more{position:absolute;left:543px;top:400px;background:#fff;color:var(--green-dark)}

/* news */
.news{position:absolute;left:0;top:2490px;width:1200px;height:678px;background:#fff}
.news h2{position:absolute;left:170px;top:55px;font:700 30px "Roboto Condensed",sans-serif}
.news-item{position:absolute;left:170px;width:420px;height:118px;background:var(--green-pale);padding:12px 12px 12px 112px}
.news-thumb{position:absolute;left:12px;top:12px;width:90px;height:90px;background:#fff;display:flex;align-items:center;justify-content:center}
.news-thumb i{width:44px;height:40px;background:var(--green-dark);border-radius:4px}
.news-thumb.photo{background:linear-gradient(135deg,#b04a4a,#e3b7a0)}
.news-item h3{font:500 14px "Roboto",sans-serif;color:var(--ink);line-height:1.5}
.news-item .meta{font-size:10px;color:#777;margin-top:4px}
.news .btn-more{position:absolute;left:170px;top:600px}
.promo{position:absolute;left:610px;top:60px;width:420px;height:558px;background:var(--yellow)}
.promo h3{position:absolute;left:20px;top:22px;width:380px;text-align:center;font:700 28px "Roboto Condensed",sans-serif;color:var(--green-dark);line-height:1.2}
.promo-band{position:absolute;left:0;top:140px;width:420px;height:160px;background:var(--green)}
.promo-band .txt{position:absolute;left:0;top:56px;width:420px;text-align:center;color:#fff;font-family:"Roboto Condensed",sans-serif}
.promo-band .t1{font-size:42px;font-weight:700;line-height:1}
.promo-band .t2{font-size:28px;line-height:1.1}
.promo-band .t3{font-size:38px;font-weight:700;color:var(--yellow);line-height:1.1}
.promo-photo{position:absolute;left:20px;top:318px;width:380px;height:150px;background:linear-gradient(100deg,#c9b39f,#8a7a6a 55%,#4a5a3a)}
.promo-mark{position:absolute;left:185px;top:452px;width:50px;height:46px;background:var(--green-dark);border-radius:4px}
.promo .btn-more{position:absolute;left:160px;top:510px}

/* bins */
.bins{position:absolute;left:0;top:3168px;width:515px;height:301px;background:#a4d07d;text-align:center}
.bins-mark{position:absolute;left:227px;top:48px;width:62px;height:56px;background:var(--green-dark);border-radius:5px}
.bins h3{position:absolute;left:0;top:140px;width:515px;font:400 24px "Roboto",sans-serif;color:var(--green-dark)}
.bins .icons{position:absolute;left:0;top:182px;width:515px;display:flex;justify-content:center;gap:26px}
.bins .b1{position:absolute;left:0;top:228px;width:515px;font:500 13px "Roboto",sans-serif;color:var(--green-dark)}
.bins .b2{position:absolute;left:0;top:248px;width:515px;font-size:12px;color:var(--green-dark)}
.map{position:absolute;left:515px;top:3168px;width:685px;height:301px;background:linear-gradient(120deg,#e8e2d0 0%,#eae6d6 55%,#aacbe8 75%,#8dbde6 100%)}

/* footer */
.site-footer{position:absolute;left:0;top:3469px;width:1200px;height:297px;background:var(--footer);color:#ddd}
.fcol{position:absolute;top:38px;font-size:12px;line-height:1.55}
.fcol h4{font:700 13px "Roboto",sans-serif;color:#fff;margin-bottom:14px}
.social{display:flex;gap:10px}
.social i{width:30px;height:30px;border:2px solid #ddd;border-radius:50%;display:block}
.ffind h4{font-size:19px;font-weight:500}
.ffind .field{display:flex;margin-top:4px}
.ffind .field span{width:180px;height:34px;background:#fff;color:#999;font-size:13px;padding:9px 10px}
.ffind .field b{width:84px;height:34px;background:var(--yellow);color:var(--green-dark);font:700 14px "Roboto Condensed",sans-serif;text-align:center;line-height:34px}
.badges{position:absolute;left:758px;top:168px;display:flex;gap:22px;align-items:center}
.badges i{width:48px;height:48px;border:3px solid #ccc;border-radius:50%;display:block}
.badges i.seal{background:var(--yellow-deep);border:none;width:58px;height:58px}
.copy{position:absolute;left:0;top:246px;width:1200px;border-top:1px solid #3a3a3a;padding:18px 0 0 170px;font-size:11px;color:#aaa}
</style>
</head>
<body>

<header class="site-header">
  <div class="brand">
    <span class="brand-mark"></span>
    <div><div class="brand-name">Brightwell Giving</div><div class="brand-tag">Think Globally while Donating Locally</div></div>
  </div>
  <svg class="phone-icon" width="30" height="30" viewBox="0 0 24 24"><path fill="#2f5d14" d="M6.6 10.8a15.1 15.1 0 0 0 6.6 6.6l2.2-2.2a1 1 0 0 1 1-.25 11.4 11.4 0 0 0 3.6.57 1 1 0 0 1 1 1V20a1 1 0 0 1-1 1A17 17 0 0 1 3 4a1 1 0 0 1 1-1h3.5a1 1 0 0 1 1 1c0 1.25.2 2.45.57 3.57a1 1 0 0 1-.25 1z"/></svg>
  <div class="phone" style="left:592px">Toll Free:<b>(855) 555-0142</b></div>
  <div class="phone" style="left:745px">New York:<b>(855) 555-0142</b></div>
  <div class="donate-now">DONATE NOW</div>
</header>

<nav class="main-nav">
  <a class="active">HOME</a><a>MISSIONS ▾</a><a>HOW IT WORKS</a><a>ABOUT US ▾</a><a>SPONSORS</a><a>NEWS</a><a>DONATE</a><a>WALL OF NEEDS</a>
</nav>

<section class="hero" role="img" aria-label="Photo of smiling volunteers sorting donated clothing into a box outdoors">
  <div class="hero-title"><div class="line1">Think Globally While Donating Locally</div><div class="line2">Brightwell Giving</div></div>
  <div class="bin-visual" role="img" aria-label="Green clothing donation bin"></div>
  <div class="finder">
    <div class="finder-label">
      <svg width="30" height="26" viewBox="0 0 30 26"><path d="M15 2a6 6 0 0 0-6 6c0 5 6 11 6 11s6-6 6-11a6 6 0 0 0-6-6z" fill="none" stroke="#fff" stroke-width="2"/><circle cx="15" cy="8" r="2" fill="#fff"/><path d="M2 24l6-7h14l6 7z" fill="none" stroke="#fff" stroke-width="2"/></svg>
      Find Local Donation Place</div>
    <div class="finder-input">Zip</div>
    <div class="finder-btn">SEARCH</div>
  </div>
</section>

<section class="welcome">
  <h2>WELCOME TO <i></i> <b>BRIGHTWELL GIVING</b></h2>
  <p>Brightwell Giving is a non-profit organization that was created for one purpose: helping the less fortunate in our country's time of greatest need. Started in 2007, Brightwell Giving has been a dedicated member of its local communities over the past four years. The company's clothing collection efforts have allowed it to provide some of the neediest members of the community to clothe themselves and their families. The company's goal is to ensure that some of the most basic needs of the community's members are met thru the philanthropic efforts of the organizations members and contributors.</p>
  <span class="btn-more">READ MORE ▸</span>
</section>

<section class="values" role="img" aria-label="Photo of green clothing donation bins on a trailer with a volunteer standing beside them">
  <div class="value-card" style="left:264px;top:112px">We Are An Open Book Organization</div>
  <div class="value-card" style="left:497px;top:112px">We Are A True 501(C)(3) Non-Profit Organization</div>
  <div class="value-card" style="left:728px;top:112px">Our Goal Is To Be With And Within The Community</div>
  <div class="value-card" style="left:264px;top:235px">Support Anti-Gun Violence</div>
  <div class="value-card" style="left:497px;top:235px">Help Disaster Victims Of Hurricane Irene</div>
  <div class="value-card" style="left:728px;top:235px">Help Valley Parent &amp; Child Society</div>
</section>

<section class="recipients">
  <span class="rec-mark"></span>
  <h2>DONATION RECEPIENTS</h2>
  <div class="sub">Think Globally while Donating Locally</div>
  <span class="btn-more">READ MORE ▸</span>
  <div class="bar" style="left:497px;width:60px;height:67px"></div>
  <div class="bar" style="left:602px;width:56px;height:133px"></div>
  <div class="bar" style="left:713px;width:55px;height:190px"></div>
  <div class="bar" style="left:821px;width:55px;height:253px"></div>
  <div class="bar" style="left:924px;width:60px;height:311px"></div>
  <div class="level" style="left:450px;top:302px"><small>LEVEL 1</small><b>$1000</b></div>
  <div class="level" style="left:556px;top:236px"><small>LEVEL 2</small><b>$1000-$2500</b></div>
  <div class="level" style="left:662px;top:179px"><small>LEVEL 3</small><b>$2500-$5000</b></div>
  <div class="level" style="left:770px;top:116px"><small>LEVEL 4</small><b>$5000-$10000</b></div>
  <div class="level" style="left:876px;top:58px;width:158px"><small>LEVEL 5</small><b>$10,000-$25000</b></div>
</section>
<div class="baseline" style="top:1953px"></div>

<section class="how">
  <div class="how-top"></div>
  <div class="ghost">A LOCAL SOLUTION TO A GLOBAL PROBLEM</div>
  <div class="how-rule" style="left:360px"></div><div class="how-rule" style="left:770px"></div>
  <div class="how-ribbon">HOW IT WORKS</div>
  <svg class="abs" style="left:420px;top:195px" width="360" height="20"><path d="M0 10 Q60 0 120 10" fill="none" stroke="#fff" stroke-width="2" stroke-dasharray="5 5"/><path d="M240 10 Q300 0 360 10" fill="none" stroke="#fff" stroke-width="2" stroke-dasharray="5 5"/></svg>
  <div class="step" style="left:184px">
    <div class="step-circle"><span class="step-num">01</span><span class="inner"><svg width="50" height="50" viewBox="0 0 50 50"><rect x="8" y="6" width="34" height="40" rx="3" fill="none" stroke="#2f5d14" stroke-width="3"/><path d="M17 20l4-4h8l4 4-3 3v12H20V23z" fill="none" stroke="#2f5d14" stroke-width="2.5"/></svg></span></div>
    <p>Drop off clothing at your<br>closest donation bin.</p>
  </div>
  <div class="step" style="left:467px">
    <div class="step-circle"><span class="step-num">02</span><span class="inner"><svg width="58" height="44" viewBox="0 0 58 44"><rect x="4" y="8" width="32" height="24" fill="none" stroke="#2f5d14" stroke-width="3"/><path d="M36 16h10l8 8v8H36" fill="none" stroke="#2f5d14" stroke-width="3"/><circle cx="14" cy="36" r="5" fill="#fff" stroke="#2f5d14" stroke-width="3"/><circle cx="44" cy="36" r="5" fill="#fff" stroke="#2f5d14" stroke-width="3"/></svg></span></div>
    <p>We pick it up and take it to our<br>sorting facility</p>
  </div>
  <div class="step" style="left:749px">
    <div class="step-circle"><span class="step-num">03</span><span class="inner"><svg width="50" height="50" viewBox="0 0 50 50"><path d="M25 40S8 28 8 18a8 8 0 0 1 17-3 8 8 0 0 1 17 3c0 10-17 22-17 22z" fill="none" stroke="#2f5d14" stroke-width="3"/><circle cx="36" cy="36" r="9" fill="#fff" stroke="#2f5d14" stroke-width="2.5"/><text x="36" y="41" font-size="12" text-anchor="middle" fill="#2f5d14" font-family="Roboto,sans-serif" font-weight="700">$</text></svg></span></div>
    <p>Charities get clothing. We pay<br>you for the clothes.</p>
  </div>
  <span class="btn-more">READ MORE ▸</span>
</section>

<section class="news">
  <h2>RECENT NEWS</h2>
  <article class="news-item" style="top:112px"><div class="news-thumb"><i></i></div><h3>Brightwell Giving created the flyer for inform the people in Manhattan to help others by giving donation.</h3><div class="meta">MAY 16, 2017 • CATEGORIES: MAIN • BY ADMIN</div></article>
  <article class="news-item" style="top:234px"><div class="news-thumb"><i></i></div><h3>We are starting the charity projects to collect funds on CrowdGive</h3><div class="meta">APRIL 28, 2017 • CATEGORIES: MAIN • BY ADMIN</div></article>
  <article class="news-item" style="top:356px"><div class="news-thumb photo" role="img" aria-label="Photo of a child"></div><h3>CHARITY PROJECT LOVE THY NEIGHBOR</h3><div class="meta">APRIL 18, 2017 • CATEGORIES: MAIN • BY ADMIN</div></article>
  <article class="news-item" style="top:478px"><div class="news-thumb"><i></i></div><h3>Charity Project LOVE THY NEIGHBOR donation boxes</h3><div class="meta">APRIL 11, 2017 • CATEGORIES: MAIN • BY ADMIN</div></article>
  <span class="btn-more">READ MORE ▸</span>

  <aside class="promo">
    <h3>Brightwell Giving Donated to Orphan House In Ukraine</h3>
    <div class="promo-band"><svg class="abs" style="left:0;top:-1px" width="420" height="40"><path d="M0 0h420L210 38z" fill="#f6c800"/></svg>
      <div class="txt"><div class="t1">DONATION</div><div class="t2">IN EUROPE</div><div class="t3">“UKRAINE”</div></div></div>
    <div class="promo-photo" role="img" aria-label="Photos of a baby and volunteers delivering donations at an orphan house"></div>
    <span class="promo-mark"></span>
    <span class="btn-more">READ MORE ▸</span>
  </aside>
</section>

<section class="bins">
  <span class="bins-mark"></span>
  <h3>Brightwell Giving Bins</h3>
  <div class="icons">
    <svg width="26" height="26" viewBox="0 0 24 24"><path d="M12 2l3 7h7l-5.5 4.5 2 7.5L12 16.5 5.5 21l2-7.5L2 9h7z" fill="none" stroke="#2f5d14" stroke-width="1.6"/></svg>
    <svg width="26" height="26" viewBox="0 0 24 24"><path d="M4 12v8h16v-8M12 3v12M7 8l5-5 5 5" fill="none" stroke="#2f5d14" stroke-width="1.6"/></svg>
    <svg width="26" height="26" viewBox="0 0 24 24"><path d="M3 9V3h6M21 9V3h-6M3 15v6h6M21 15v6h-6" fill="none" stroke="#2f5d14" stroke-width="1.6"/></svg>
  </div>
  <div class="b1">Clothes Donation Bins</div>
  <div class="b2">16,368 views</div>
</section>
<div class="map" role="img" aria-label="Map of the northeastern United States with donation bin locations marked"></div>

<footer class="site-footer">
  <div class="fcol" style="left:170px"><h4>QUICK LINKS</h4>Home<br>Missions<br>How It Works<br>About Us<br>Sponsors<br>News<br>Donate<br>Wall Of Needs</div>
  <div class="fcol" style="left:331px"><h4>CONTACT US</h4>New York Office<br>42 Orchard Ln, Fairbrook, NY 12090<br>(855) 555-0142<br><br>NY Warehouse<br>118 River Rd, Milldale, NY 12470<br><br>Thrift Store<br>77 Linden St, Harborton, NY 12560</div>
  <div class="fcol" style="left:542px"><h4>FOLLOW US</h4><div class="social"><i></i><i></i><i></i></div></div>
  <div class="fcol ffind" style="left:758px;top:30px"><h4>Find Local Donation Place</h4><div class="field"><span>Zip</span><b>SEARCH</b></div></div>
  <div class="badges"><i></i><i></i><i></i><i class="seal"></i></div>
  <div class="copy">© 2018 Brightwell Giving. All Rights Reserved.</div>
</footer>

</body>
</html>
```